Business Card Design Project - Sports Brand

Lumora is a e-commerce fitness wear brand for ladies who are into gym, pole and swim.

Card should not be overly cluttered and should include the following:

1. logo
2. Name of the company (Use "Lumora Wear Pte Ltd" for now)
3. Address of company (Use a mock address)
4. Representative's name and contact info etc. (use a mock name and contact info)
5. website address

Target Market(s)

Women who are into pole , gym, and swim.

Women who shop online

Industry/Entity Type

E-Commerce

Colors

Designer to choose colors to be used in the design.

Requirements
Nice to have
• feminine sublimation of colours

Need not be printed on traditional paper. We would like the design to be revolutionary and interesting to the eye :)
Should not have
• the design should not be traditional looking. Do not include illustrations of Bikinis, yoga poses etc. in the card.

```html
<!DOCTYPE html>
<html lang="en">
<head>
<meta charset="utf-8">
<title>Lumora Wear – Business Card</title>
<link href="https://fonts.googleapis.com/css2?family=Playfair+Display:wght@400;700&family=Lora:wght@400&display=swap" rel="stylesheet">
<style>
  :root {
    --backdrop: #e6e4e1;
    --card: #ffffff;
    --rose: #e2478f;
    --crimson: #c0273a;
    --orange: #ef5a2a;
    --pink-soft: #ee9cc4;
    --ink: #555555;
    --shadow: rgba(0,0,0,0.18);
  }
  * { margin: 0; padding: 0; box-sizing: border-box; }
  html, body { width: 1200px; height: 1000px; overflow: hidden; }
  body {
    background: var(--backdrop);
    font-family: "Lora", Georgia, serif;
    position: relative;
  }
  .card {
    position: absolute;
    top: 150px;
    width: 400px;
    height: 700px;
    background: var(--card);
    box-shadow: 0 10px 24px var(--shadow);
    overflow: hidden;
  }
  .card--front { left: 150px; }
  .card--back { left: 650px; }

  .wash {
    position: absolute;
    left: 0; top: 0;
    width: 100%;
    height: 240px;
    background: linear-gradient(160deg, var(--pink-soft) 0%, var(--rose) 40%, var(--orange) 100%);
    opacity: 0.9;
  }

  .brand {
    position: absolute;
    left: 0; right: 0;
    top: 430px;
    display: flex;
    flex-direction: column;
    align-items: center;
    gap: 12px;
  }
  .brand-row { display: flex; align-items: center; gap: 14px; }
  .brand-dot {
    width: 30px; height: 30px;
    border-radius: 50%;
    background: var(--rose);
  }
  .brand-name {
    font-family: "Playfair Display", Georgia, serif;
    font-weight: 700;
    font-size: 52px;
    color: var(--crimson);
    letter-spacing: 1px;
  }
  .brand-tagline {
    font-size: 16px;
    color: var(--ink);
    letter-spacing: 1px;
  }

  .contact {
    position: absolute;
    left: 40px; right: 40px;
    top: 310px;
    text-align: right;
  }
  .person-name {
    font-family: "Playfair Display", Georgia, serif;
    font-size: 26px;
    color: var(--rose);
    letter-spacing: 2px;
  }
  .person-role { font-size: 17px; color: var(--ink); margin-top: 4px; }
  .contact-list { list-style: none; margin-top: 22px; }
  .contact-item {
    display: flex;
    justify-content: flex-end;
    align-items: center;
    gap: 10px;
    font-size: 15px;
    color: var(--ink);
    margin-bottom: 10px;
  }
  .contact-icon { width: 22px; height: 22px; flex: none; }
  .company {
    font-family: "Playfair Display", Georgia, serif;
    font-size: 19px;
    color: var(--rose);
    letter-spacing: 1.5px;
    margin-top: 24px;
  }
  .address { font-size: 15px; color: var(--ink); margin-top: 6px; line-height: 1.5; }
</style>
</head>
<body>
  <section class="card card--front">
    <div class="wash" role="img" aria-label="Pink to orange watercolour wash"></div>
    <div class="brand">
      <div class="brand-row">
        <span class="brand-dot"></span>
        <span class="brand-name">Lumora</span>
      </div>
      <p class="brand-tagline">Yoga · Swim · Pole</p>
    </div>
  </section>

  <section class="card card--back">
    <div class="wash" role="img" aria-label="Pink to orange watercolour wash"></div>
    <div class="contact">
      <h1 class="person-name">MARA ELLIS</h1>
      <p class="person-role">Director</p>
      <ul class="contact-list">
        <li class="contact-item">555 204 3318
          <svg class="contact-icon" viewBox="0 0 22 22"><circle cx="11" cy="11" r="11" fill="#e2478f"/><path d="M8 6.5c-.8.6-1.3 1.5-.8 3 .7 2 2.3 3.7 4.3 4.6 1.4.6 2.4.1 3-.7l-1.6-1.5-1.1.6c-.9-.4-1.8-1.3-2.2-2.2l.6-1.1z" fill="#fff"/></svg>
        </li>
        <li class="contact-item">mara.ellis@mailbox.com
          <svg class="contact-icon" viewBox="0 0 22 22"><circle cx="11" cy="11" r="11" fill="#e2478f"/><rect x="6" y="7.5" width="10" height="7" fill="#fff"/><path d="M6 7.5l5 4 5-4" fill="none" stroke="#e2478f" stroke-width="1"/></svg>
        </li>
        <li class="contact-item">www.lumorawear.com
          <svg class="contact-icon" viewBox="0 0 22 22"><circle cx="11" cy="11" r="11" fill="#e2478f"/><g fill="none" stroke="#fff" stroke-width="1.2"><circle cx="11" cy="11" r="5.5"/><ellipse cx="11" cy="11" rx="2.4" ry="5.5"/><path d="M5.5 11h11"/></g></svg>
        </li>
      </ul>
      <h2 class="company">LUMORA WEAR PTE. LTD.</h2>
      <p class="address">18 Orchid Lane,<br>Singapore 428910</p>
    </div>
  </section>
</body>
</html>
```